Building company requiring web site design

We need a web design for a new company based in Sydney called Marlow Building Co. We build and renovate new and existing homes for consumers. We would like to see design that use the colours red and grey. The final design should communicate innovative building but with old fashion quality, great customer service and attention to detail. I have already had a logo and stationary design completed and would like to use the these colour schemes
Updates

Target Market(s)

Home owners, investors

Industry/Entity Type

Building

Coding

Coded - Design and coding required

Number of Pages Required

5+ page

Requirements
Must have
• Home page, contact page, about us page, gallery page and testimonial page
Nice to have
• Contact form

```html
<!DOCTYPE html>
<html lang="en">
<head>
<meta charset="utf-8">
<title>Marlow Building Co.</title>
<link rel="stylesheet" href="https://fonts.googleapis.com/css2?family=Montserrat:wght@300;400;500;600;700&display=swap">
<style>
:root{
  --red:#e8104a;
  --ink:#222426;
  --charcoal:#2e2f2f;
  --footer:#2f3031;
  --footer-bar:#3a3b3d;
  --mist:#eef3f5;
  --white:#ffffff;
  --muted:#9a9c9e;
}
*{box-sizing:border-box;margin:0;padding:0}
html,body{width:1000px;height:1200px;overflow:hidden;background:var(--white)}
body{font-family:'Montserrat',sans-serif;color:var(--ink);position:relative}
.page{position:absolute;left:283px;top:0;width:436px;height:1200px;background:var(--white)}
.abs{position:absolute}
.accent{color:var(--red)}

/* header */
.brand{left:14px;top:10px;font-size:6.5px;font-weight:700;color:var(--ink);white-space:nowrap}
.nav{top:7px;font-size:5px;font-weight:500;letter-spacing:.1px;white-space:nowrap}
.search{left:415px;top:20px;width:14px;height:8px;border:1px solid var(--ink);border-radius:5px}

/* hero */
.hero{left:0;top:32px;width:436px;height:237px;background:linear-gradient(180deg,#5b6160 0%,#4a504f 45%,#3a3d3d 75%,#2d2f30 100%)}
.hero-title{left:0;width:436px;text-align:center;color:var(--white);font-weight:300;font-size:20px;line-height:1}
.hero-title b{font-weight:500}
.scroll-cue{left:202px;top:184px}

/* light body */
.mist{left:0;top:269px;width:436px;height:653px;background:var(--mist)}
.heading{left:0;width:436px;text-align:center;font-weight:300;white-space:nowrap}
.intro{left:60px;width:316px;top:310px;text-align:center;font-size:9.5px;line-height:10.5px;font-weight:400}
.rule{height:1px;background:linear-gradient(90deg,transparent,#6b6d6f 30%,#6b6d6f 70%,transparent)}

.service-panel{background:var(--charcoal);color:var(--white);font-size:7.4px;line-height:8.2px;font-weight:400}
.service-name{color:var(--red);font-weight:700;font-size:17px;text-align:center;width:200px}

.avatar{width:34px;height:34px;border-radius:50%;background:radial-gradient(circle at 50% 40%,#b9bcbf,#6e7174)}
.client{font-size:8px;font-weight:700;text-align:center;width:120px}
.quote{font-size:10px;line-height:12px;font-weight:400;white-space:nowrap}
.quote-mark{font-size:26px;font-weight:700;line-height:1;font-family:'Georgia',serif}
.see-all{left:192px;top:811px;width:52px;height:18px;border-radius:9px;background:var(--red);color:var(--white);font-size:9.5px;text-align:center;line-height:18px}

/* map */
.map{left:0;top:922px;width:436px;height:184px;background:linear-gradient(135deg,#e6e1d8 0%,#ddd8cf 55%,#9fc3f2 75%,#8bb6ee 100%)}
.map-label{left:288px;top:944px;font-size:12px;font-weight:500;color:var(--ink);background:rgba(200,200,200,.6);padding:1px 4px;white-space:nowrap}

/* footer */
.footer{left:0;top:1118px;width:436px;height:82px;background:var(--footer)}
.contact{left:5px;top:1135px;font-size:6px;line-height:10px;color:var(--white)}
.newsletter{left:152px;top:1134px;width:128px;height:14px;border:1px solid #6a6c6e;border-radius:7px;font-size:5px;color:var(--muted);line-height:12px;padding-left:10px}
.social{top:1137px;width:8px;height:8px;border-radius:50%;background:#6f7173}
.social.on{width:14px;height:14px;top:1134px;background:var(--red);box-shadow:0 0 6px rgba(232,16,74,.7)}
.footer-bar{left:8px;top:1168px;width:417px;height:22px;background:var(--footer-bar)}
.footer-link{top:1177px;font-size:5px;color:var(--muted);white-space:nowrap}
</style>
</head>
<body>
<div class="page">
  <!-- header -->
  <div class="abs brand">Marlow Building Co.</div>
  <div class="abs nav" style="left:248px">HOME</div>
  <div class="abs nav" style="left:283px">GALLERY</div>
  <div class="abs nav" style="left:318px">TESTIMNOL</div>
  <div class="abs nav" style="left:359px">ABOUT US</div>
  <div class="abs nav" style="left:399px">CONTACT US</div>
  <div class="abs search">
    <svg width="12" height="6" viewBox="0 0 12 6" style="position:absolute;left:0;top:0"><circle cx="5.6" cy="2.7" r="1.5" fill="none" stroke="#222" stroke-width=".7"/><line x1="6.7" y1="3.8" x2="7.7" y2="4.8" stroke="#222" stroke-width=".7"/></svg>
  </div>

  <!-- hero -->
  <div class="abs hero" role="img" aria-label="Street photo of a vintage car parked in front of a house with a white picket fence"></div>
  <div class="abs hero-title" style="top:68px">Still living in a <b>house?</b></div>
  <div class="abs hero-title" style="top:97px">or</div>
  <div class="abs hero-title" style="top:122px">Still dreaming about a <b>house?</b></div>
  <svg class="abs scroll-cue" width="30" height="30" viewBox="0 0 30 30"><circle cx="15" cy="15" r="13" fill="none" stroke="#fff" stroke-width="1.6"/><polyline points="8.5,12.5 15,19 21.5,12.5" fill="none" stroke="#fff" stroke-width="1.6"/></svg>

  <!-- who we are -->
  <div class="abs mist"></div>
  <div class="abs heading" style="top:283px;font-size:16px">Who are we ?</div>
  <div class="abs intro"><span class="accent">We</span> are a company that build and renovate new and existing homes for consumers.</div>
  <div class="abs rule" style="left:175px;top:357px;width:77px"></div>

  <!-- services -->
  <div class="abs heading" style="top:376px;font-size:15px"><span class="accent">Our</span> services</div>

  <div class="abs service-name" style="left:-6px;top:406px">Building</div>
  <svg class="abs" style="left:73px;top:442px" width="42" height="46" viewBox="0 0 42 46">
    <path d="M28 12 A15 15 0 1 0 36 26" fill="none" stroke="#222" stroke-width="5"/>
    <line x1="21" y1="30" x2="33" y2="11" stroke="#222" stroke-width="5"/>
    <polygon points="26,8 38,2 38,16" fill="#222"/>
  </svg>
  <div class="abs service-panel" style="left:220px;top:403px;width:216px;height:107px;padding:15px 6px 0 7px">Lorem ipsum dolor sit amet, consectetur adipiscing elit. Vestibulum nibh elit, auctor cursus turpis in, euismod porta est. In eget erat vel felis porta porta vitae in ante. Donec finibus tincidunt tempus. Donec tincidunt odio ex, non volutpat risus sagittis ut. Vestibulum at nunc eros.</div>

  <div class="abs service-panel" style="left:0;top:511px;width:219px;height:107px;padding:19px 2px 0 8px;text-align:right">Lorem ipsum dolor sit amet, consectetur adipiscing elit. Vestibulum nibh elit, auctor cursus turpis in, euismod porta est. In eget erat vel felis porta porta vitae in ante. Donec finibus tincidunt tempus. Donec tincidunt odio ex, non volutpat risus sagittis ut. Vestibulum at nunc eros.</div>
  <div class="abs service-name" style="left:236px;top:518px">Renovating</div>
  <svg class="abs" style="left:306px;top:552px" width="42" height="42" viewBox="0 0 42 42">
    <path d="M7 19 A14 14 0 0 1 32 11" fill="none" stroke="#222" stroke-width="5"/>
    <polygon points="27,4 38,4 38,16" fill="#222"/>
    <path d="M35 23 A14 14 0 0 1 10 31" fill="none" stroke="#222" stroke-width="5"/>
    <polygon points="15,38 4,38 4,26" fill="#222"/>
  </svg>

  <!-- testimonials -->
  <div class="abs rule" style="left:147px;top:659px;width:135px"></div>
  <div class="abs heading" style="top:670px;font-size:13px">what <span class="accent">our</span> customers say...</div>

  <div class="abs avatar" style="left:73px;top:711px" role="img" aria-label="Client portrait"></div>
  <div class="abs client" style="left:30px;top:749px">Client <span class="accent">Name</span></div>
  <div class="abs quote-mark" style="left:19px;top:767px">&ldquo;</div>
  <div class="abs quote" style="left:40px;top:769px">Lorem ipsum dolor sit amet,<br>consectetur adipiscing elit.....</div>

  <div class="abs avatar" style="left:303px;top:711px" role="img" aria-label="Client portrait"></div>
  <div class="abs client" style="left:260px;top:749px">Client <span class="accent">Name</span></div>
  <div class="abs quote-mark" style="left:249px;top:767px">&ldquo;</div>
  <div class="abs quote" style="left:270px;top:769px">Lorem ipsum dolor sit amet,<br>consectetur adipiscing elit.....</div>

  <div class="abs see-all">See All &gt;</div>
  <div class="abs rule" style="left:179px;top:851px;width:78px"></div>

  <!-- location -->
  <div class="abs heading" style="top:881px;font-size:13px"><span class="accent">We</span> are here...</div>
  <div class="abs map" role="img" aria-label="Street map of central Sydney showing the company location by the harbour"></div>
  <svg class="abs" style="left:267px;top:942px" width="18" height="28" viewBox="0 0 18 28"><path d="M9 1 C4 1 1 5 1 9 C1 15 9 27 9 27 C9 27 17 15 17 9 C17 5 14 1 9 1Z" fill="#e8104a"/><circle cx="9" cy="9" r="3" fill="#fff"/></svg>
  <div class="abs map-label"><span class="accent">Marlow</span> Building Co.</div>

  <!-- footer -->
  <div class="abs footer"></div>
  <div class="abs contact">admin@marlowbuildingco.com.au<br>0400 555 018</div>
  <div class="abs newsletter">Subscribe to our Newsletter
    <svg width="8" height="7" viewBox="0 0 8 7" style="position:absolute;right:7px;top:3px"><polygon points="0,0 8,3.5 0,7 1.5,3.5" fill="none" stroke="#9a9c9e" stroke-width=".7"/></svg>
  </div>
  <div class="abs social" style="left:354px"></div>
  <div class="abs social" style="left:369px"></div>
  <div class="abs social" style="left:384px"></div>
  <div class="abs social on" style="left:395px"></div>
  <div class="abs social" style="left:414px"></div>
  <div class="abs footer-bar"></div>
  <div class="abs footer-link" style="left:19px">Privacy Policy</div>
  <div class="abs footer-link" style="left:74px">Terms of Use</div>
  <div class="abs footer-link" style="left:372px">Back to top</div>
  <svg class="abs" style="left:409px;top:1177px" width="6" height="5" viewBox="0 0 6 5"><polyline points="1,4 3,1.5 5,4" fill="none" stroke="#9a9c9e" stroke-width=".8"/></svg>
</div>
</body>
</html>
```